Create Premium Wine Label Design

We are premium wine exporters from Australia. We are looking to introduce new brand " The Velloro" - in red wine, White wine and Sparkling wine to international market.

The sample label design for red wine ( Shiraz) is attached.

This is our luxury brand. We need a stunning wine label designs for (front, back and neck) that should be mostly in GOLD colour and design should be really eye catching.

We have provided sample design for front, back and neck labels. However, we are looking forward to see a completely new improvised design.

LOGO attached.

Front Label Design Specification:

* We would like to see designs that are in Gold colour.
* Wine Bottle size is standard: 750ml; we assume the same design can be resizable to different bottle sizes.
* Our design should suit both black, white and sparkling wine bottles(sample attached)
* Use our logo in the design (see attached - label sample)
* Content for front label (see attached).
* Design should include all information specified in the sample

Back Label Design
* All contents in the sample should be used ( sample attached)
* LOGO attached.

Neck Label Design
* Sample of Neck label attached, please provide similar or your own design.
* LOGO attached.

Image Samples:
* Samples of label designs we like (see attached)
* Sample for gold color (see attached)
* For bottle shapes (see attached)
* Front, Back and Neck Label Samples (see attached)

Target Market(s)

International Wine Market

Font styles to use
Decorative
Script

Requirements
Must have
• Must have golden color on front and back label

```html
<!DOCTYPE html>
<html lang="en">
<head>
<meta charset="utf-8">
<title>Brimwood Shiraz – The Velloro – Front Label</title>
<link rel="stylesheet" href="https://fonts.googleapis.com/css2?family=Tinos:ital,wght@0,700;1,400&display=swap">
<style>
  :root {
    --page: #ffffff;
    --glass: #1c1719;
    --label: #1f2b35;
    --label-edge: #2c3a46;
    --gold: #d9a93a;
    --gold-light: #f3d27a;
    --copper: #c87a45;
    --copper-dark: #8a4a25;
    --yellow: #f6ec1c;
    --ink: #1a1a1a;
  }
  * { margin: 0; padding: 0; box-sizing: border-box; }
  html, body {
    width: 1200px;
    height: 3214px;
    overflow: hidden;
    background: var(--page);
  }
  .canvas {
    position: relative;
    width: 1200px;
    height: 3214px;
    font-family: "Tinos", "Times New Roman", serif;
  }

  /* Neck label */
  .neck-label {
    position: absolute;
    left: 493px;
    top: 139px;
    width: 247px;
    height: 504px;
    background: var(--label);
    border-radius: 12px;
  }
  .neck-label .rule {
    position: absolute;
    left: 0;
    width: 100%;
    height: 10px;
    background: linear-gradient(var(--copper), var(--copper-dark));
  }
  .neck-label .rule.top { top: 156px; }
  .neck-label .rule.bottom { top: 439px; }
  .neck-label .brand {
    position: absolute;
    top: 280px;
    width: 100%;
    text-align: center;
    font-weight: 700;
    font-size: 34px;
    line-height: 40px;
    letter-spacing: 1px;
    color: var(--gold);
  }

  /* Printed glass area */
  .glass {
    position: absolute;
    left: 290px;
    top: 1000px;
    width: 640px;
    height: 1946px;
    background: var(--glass);
    border-radius: 60px;
  }

  /* Front label */
  .front-label {
    position: absolute;
    left: 300px;
    top: 1264px;
    width: 620px;
    height: 1147px;
  }
  .front-label svg { position: absolute; inset: 0; }
  .brand-mark {
    position: absolute;
    left: 280px;
    top: 334px;
    width: 60px;
    height: 60px;
    border-radius: 50%;
    background: var(--gold);
  }
  .brand-name {
    position: absolute;
    top: 476px;
    width: 100%;
    text-align: center;
    font-weight: 700;
    font-size: 62px;
    line-height: 68px;
    letter-spacing: 2px;
    color: var(--gold);
  }
  .flourish {
    position: absolute;
    left: 140px;
    top: 540px;
    width: 340px;
    height: 40px;
    background: linear-gradient(90deg, transparent, var(--gold) 25%, var(--gold-light) 50%, var(--gold) 75%, transparent);
    opacity: 0.8;
    border-radius: 20px;
  }
  .varietal {
    position: absolute;
    top: 722px;
    width: 100%;
    text-align: center;
    font-weight: 700;
    font-size: 120px;
    line-height: 120px;
    color: var(--yellow);
  }
  .cuvee {
    position: absolute;
    top: 854px;
    width: 100%;
    text-align: center;
    font-style: italic;
    font-size: 64px;
    line-height: 72px;
    color: var(--yellow);
  }

  .vintage {
    position: absolute;
    top: 2638px;
    width: 100%;
    text-align: center;
    font-weight: 700;
    font-size: 106px;
    line-height: 106px;
    letter-spacing: 4px;
    color: var(--yellow);
  }
  .origin {
    position: absolute;
    top: 2774px;
    width: 100%;
    text-align: center;
    font-weight: 700;
    font-size: 40px;
    line-height: 46px;
    color: var(--yellow);
  }

  .view-caption {
    position: absolute;
    top: 2994px;
    width: 100%;
    text-align: center;
    font-weight: 700;
    font-size: 92px;
    line-height: 98px;
    color: var(--ink);
  }
</style>
</head>
<body>
<main class="canvas">

  <section class="neck-label" aria-label="Neck label">
    <div class="rule top"></div>
    <div class="brand">BRIMWOOD</div>
    <div class="rule bottom"></div>
  </section>

  <div class="glass"></div>

  <section class="front-label" aria-label="Front label">
    <svg viewBox="0 0 620 1147" width="620" height="1147" aria-hidden="true">
      <defs>
        <linearGradient id="goldLine" x1="0" y1="0" x2="1" y2="1">
          <stop offset="0" stop-color="#f3d27a"/>
          <stop offset="0.5" stop-color="#c8912c"/>
          <stop offset="1" stop-color="#f0c866"/>
        </linearGradient>
      </defs>
      <path fill="#2c3a46" d="M0,130 Q20,130 20,110 L180,110 Q200,110 212,80 Q236,0 290,0 L330,0 Q384,0 408,80 Q420,110 440,110 L600,110 Q600,130 620,130 L620,1017 Q600,1017 600,1037 L440,1037 Q420,1037 408,1067 Q384,1147 330,1147 L290,1147 Q236,1147 212,1067 Q200,1037 180,1037 L20,1037 Q20,1017 0,1017 Z"/>
      <path fill="#1f2b35" d="M10,138 Q28,138 28,120 L182,120 Q204,120 217,88 Q240,10 290,10 L330,10 Q380,10 403,88 Q416,120 438,120 L592,120 Q592,138 610,138 L610,1009 Q592,1009 592,1027 L438,1027 Q416,1027 403,1059 Q380,1137 330,1137 L290,1137 Q240,1137 217,1059 Q204,1027 182,1027 L28,1027 Q28,1009 10,1009 Z"/>
      <path fill="none" stroke="url(#goldLine)" stroke-width="5" d="M22,148 Q40,148 40,130 L186,130 Q208,130 222,98 Q244,24 292,24 L328,24 Q376,24 398,98 Q412,130 434,130 L580,130 Q580,148 598,148 L598,999 Q580,999 580,1017 L434,1017 Q412,1017 398,1049 Q376,1123 328,1123 L292,1123 Q244,1123 222,1049 Q208,1017 186,1017 L40,1017 Q40,999 22,999 Z"/>
    </svg>
    <span class="brand-mark"></span>
    <div class="brand-name">BRIMWOOD</div>
    <span class="flourish" role="img" aria-label="Gold ornamental flourish beneath the brand name"></span>
    <div class="varietal">SHIRAZ</div>
    <div class="cuvee">The Velloro</div>
  </section>

  <div class="vintage">2018</div>
  <div class="origin">WINE OF AUSTRALIA</div>

  <div class="view-caption">FRONT</div>

</main>
</body>
</html>
```